Therapy Services & Training

I provide counseling/therapy to individuals and families. I also travel the country and provide training at conferences.
I would like to see a card which takes my company name and design a logo using the letters "HWAE".
Target Market(s)
Therapists, non-profit organizations, clients looking for therapy
Industry/Entity Type
Training
Contact Information for Business Card
Harborview Wellness Advising & Education LLC
Delia Marsh, M.S.W., LCSW
Clinical Therapist & Trainer
Providing clinical therapy services to individuals, families, couples & children. We also provide life coaching and crisis training.
counselordelia@mailbrook.net
www.harborviewwellnessadvising.com
(555) 214-3092
Cedarvale, IL 60412
(BACK SIDE OF CARD)
We are certified by the Ongoing Professional Lawyer Studies (OPLS) Council of the Prairie High Tribunal to provide Continuing Legal Education (CLE) credits to Illinois attorneys. Call about what courses we offer! (555) 214-3092

```html
<!DOCTYPE html>
<html lang="en">
<head>
<meta charset="utf-8">
<title>Harborview Wellness Advising & Education – Business Card</title>
<link href="https://fonts.googleapis.com/css2?family=Lato:wght@400;700;900&display=swap" rel="stylesheet">
<style>
  :root {
    --backdrop: #e4e2df;
    --card-dark: #2f2f31;
    --card-light: #ffffff;
    --ink: #222222;
    --on-dark: #f2f2f2;
    --blue: #7dbde6;
    --pink: #c8479b;
    --green: #6cc06a;
  }
  * { box-sizing: border-box; margin: 0; padding: 0; }
  html, body {
    width: 1200px; height: 1000px; overflow: hidden;
    background: var(--backdrop);
    font-family: "Lato", sans-serif;
  }
  .canvas {
    width: 1200px; height: 1000px;
    display: flex; flex-direction: column; align-items: center; justify-content: center;
    gap: 40px;
  }
  .card {
    position: relative;
    width: 760px; height: 434px;
    box-shadow: 0 10px 28px rgba(0,0,0,.18);
    overflow: hidden;
  }
  .stripe {
    position: absolute; left: 0; right: 0; bottom: 0; height: 12px;
    display: flex;
  }
  .stripe span { flex: 1; }
  .stripe .blue { background: var(--blue); }
  .stripe .pink { background: var(--pink); }
  .stripe .green { background: var(--green); }

  /* Front */
  .card-front { background: var(--card-dark); color: var(--on-dark); }
  .front-header {
    position: absolute; top: 58px; left: 70px; right: 60px;
    display: flex; align-items: center; justify-content: space-between;
  }
  .brand { display: flex; align-items: center; gap: 14px; }
  .brand-dot { width: 46px; height: 46px; border-radius: 50%; background: var(--blue); }
  .brand-name { font-weight: 900; font-size: 62px; letter-spacing: 2px; color: var(--on-dark); line-height: 1; }
  .company-name {
    color: var(--blue); font-weight: 700; font-size: 21px; letter-spacing: 1.5px;
    text-transform: uppercase; text-align: center; line-height: 1.2;
  }
  .tagline {
    position: absolute; top: 170px; left: 70px; right: 60px;
    text-align: center; font-size: 19px; letter-spacing: .6px; line-height: 1.35;
  }
  .front-footer {
    position: absolute; top: 290px; left: 60px; right: 50px;
    display: flex; align-items: stretch; gap: 22px;
  }
  .person { flex: 1; text-align: right; font-size: 18px; line-height: 1.3; }
  .person-name { color: var(--pink); font-size: 25px; text-transform: uppercase; letter-spacing: .5px; }
  .person-name .credentials { color: var(--green); font-size: 17px; text-transform: none; }
  .divider { width: 2px; background: var(--blue); }
  .contact { flex: 1.25; font-size: 17px; line-height: 1.4; letter-spacing: .3px; }

  /* Back */
  .card-back { background: var(--card-light); color: var(--ink); text-align: center; }
  .back-brand {
    position: absolute; top: 52px; left: 0; right: 0;
    display: flex; align-items: center; justify-content: center; gap: 18px;
  }
  .back-brand .brand-dot { width: 70px; height: 70px; }
  .back-brand .brand-name { color: var(--blue); font-size: 92px; }
  .statement {
    position: absolute; top: 190px; left: 50px; right: 50px;
    font-size: 22px; font-weight: 700; line-height: 1.35;
  }
  .statement .accent-green { color: var(--green); }
  .statement .accent-pink { color: var(--pink); }
  .call { margin-top: 14px; font-size: 21px; font-weight: 700; }
  .call-number { display: block; color: var(--blue); font-size: 34px; font-weight: 700; letter-spacing: .5px; }
</style>
</head>
<body>
<main class="canvas">
  <section class="card card-front">
    <header class="front-header">
      <div class="brand">
        <span class="brand-dot"></span>
        <span class="brand-name">HWAE</span>
      </div>
      <h1 class="company-name">Harborview Wellness Advising<br>&amp; Education LLC</h1>
    </header>
    <p class="tagline">Providing Clinical Therapy services to Individuals, Families, Couples &amp;<br>Children. We also provide Life coaching and Crisis training.</p>
    <div class="front-footer">
      <div class="person">
        <div class="person-name">Delia Marsh, <span class="credentials">M.S.W., LCSW</span></div>
        <div class="person-title">Clinical Therapist &amp; Trainer</div>
        <div class="person-location">Cedarvale, IL 60412</div>
      </div>
      <span class="divider"></span>
      <div class="contact">
        <div>(555) 214-3092</div>
        <div>counselordelia@mailbrook.net</div>
        <div>www.harborviewwellnessadvising.com</div>
      </div>
    </div>
    <div class="stripe"><span class="blue"></span><span class="pink"></span><span class="green"></span></div>
  </section>

  <section class="card card-back">
    <div class="back-brand">
      <span class="brand-dot"></span>
      <span class="brand-name">HWAE</span>
    </div>
    <p class="statement">
      We are certified by the <span class="accent-green">Ongoing Professional Lawyer Studies
      (OPLS)</span> Council of the Prairie High Tribunal to provide
      <span class="accent-pink">Continuing Legal Education (CLE)</span> credits to Illinois attorneys.
      <span class="call">Call about what courses we offer!<span class="call-number">(555) 214-3092</span></span>
    </p>
    <div class="stripe"><span class="blue"></span><span class="pink"></span><span class="green"></span></div>
  </section>
</main>
</body>
</html>
```